New Business Card Design Project

Easy part first... I want the backside to be simple... jet black background with our logo in jet black/white/color. Feel free to play with tagline ideas under the logo if you want, I'm still toying around with it myself.

The front side... I need the logo on it, my photo headshot, and the following information:

Ray T. Calloway
Top Producer
555-201-4837
calloway.ray.t@fernmail.example
www.ListNorthernNests.example
www.GetNorthernNests.example

I'm looking for creativity with font, simple, but elegant, pairs well with the logo, good visibility of my photo, black background on the front as well, clearly see and identify information.
Updates

I would like the websites to have capitalization on the first letter of each word - www.ListNorthernNests.example and www.GetNorthernNests.example Also, I would like each of the capital letters to be slightly larger than the other font

Target Market(s)

We help people buy and sell homes from $50,000 to over a $1million.

Industry/Entity Type

Business

Requirements
Must have
• Must have information from above.
Nice to have
• Introducing a new color to be sharp against the black- possibly in the silver/nickel/platinum metallics? Feel free to crop the headshot down some if needed.
Should not have
• NO CHEESY GRAPHICS

```html
<!DOCTYPE html>
<html lang="en">
<head>
<meta charset="utf-8">
<title>Northnest Realty — Business Card</title>
<link rel="stylesheet" href="https://fonts.googleapis.com/css2?family=EB+Garamond:wght@500;700&display=swap">
<style>
  :root {
    --canvas: #ffffff;
    --card: #000000;
    --ink: #ffffff;
    --gold: #b9a66a;
    --gold-soft: #8f7f4e;
    --guide: #6b6b6b;
    --photo-dark: #2a211c;
    --photo-mid: #5a4a3e;
  }
  * { margin: 0; padding: 0; box-sizing: border-box; }
  html, body { width: 1200px; height: 1000px; overflow: hidden; background: var(--canvas); }
  body { position: relative; font-family: "EB Garamond", Garamond, serif; color: var(--ink); }

  .card { position: absolute; left: 304px; width: 563px; height: 338px; background: var(--card); }
  .card--front { top: 114px; }
  .card--back { top: 563px; }

  .safe-guide { position: absolute; left: 18px; top: 18px; width: 526px; height: 302px; border: 1px solid var(--guide); }
  .crop-mark { position: absolute; width: 11px; height: 11px; }
  .crop-mark::before, .crop-mark::after { content: ""; position: absolute; background: var(--ink); }
  .crop-mark::before { left: 5px; top: 0; width: 1.5px; height: 11px; }
  .crop-mark::after { left: 0; top: 5px; width: 11px; height: 1.5px; }
  .crop-mark--tl { left: 13px; top: 13px; }
  .crop-mark--tr { right: 13px; top: 13px; }
  .crop-mark--bl { left: 13px; bottom: 13px; }
  .crop-mark--br { right: 13px; bottom: 13px; }

  .headshot {
    position: absolute; left: 41px; top: 31px; width: 163px; height: 222px;
    border: 2px solid var(--gold); border-radius: 2px;
    background: radial-gradient(ellipse at 50% 35%, var(--photo-mid), var(--photo-dark) 75%);
  }
  .agent-name { position: absolute; left: 20px; width: 205px; top: 255px; text-align: center; font-weight: 700; font-size: 22px; letter-spacing: -0.2px; }
  .agent-title { position: absolute; left: 20px; width: 205px; top: 284px; text-align: center; font-weight: 700; font-size: 15px; color: var(--gold); letter-spacing: 0.3px; }

  .brand { text-align: center; color: var(--ink); font-weight: 500; text-transform: uppercase; line-height: 1.1; }
  .brand--front { position: absolute; left: 296px; width: 226px; top: 78px; font-size: 31px; letter-spacing: 2px; }
  .brand--back { font-size: 44px; letter-spacing: 3px; }

  .contact { position: absolute; right: 37px; top: 205px; text-align: right; font-style: normal; font-weight: 500; font-size: 18px; line-height: 24.5px; }
  .contact__phone { font-weight: 700; font-size: 20px; }
  .contact__cap { font-size: 1.12em; }

  .brand-frame {
    position: absolute; left: 114px; top: 47px; width: 360px; height: 242px;
    display: flex; align-items: center; justify-content: center;
    border: 1.5px solid var(--gold-soft);
    box-shadow: inset 0 0 14px rgba(185, 166, 106, 0.45);
  }
</style>
</head>
<body>
  <section class="card card--front">
    <div class="safe-guide"></div>
    <span class="crop-mark crop-mark--tl"></span>
    <span class="crop-mark crop-mark--tr"></span>
    <span class="crop-mark crop-mark--bl"></span>
    <span class="crop-mark crop-mark--br"></span>

    <div class="headshot" role="img" aria-label="Headshot of Ray T. Calloway in a dark suit"></div>
    <p class="agent-name">Ray T. Calloway</p>
    <p class="agent-title">TOP PRODUCER</p>

    <p class="brand brand--front">Northnest<br>Realty</p>

    <address class="contact">
      <div class="contact__phone">555-201-4837</div>
      <div>calloway.ray.t@fernmail.example</div>
      <div>www.<span class="contact__cap">L</span>ist<span class="contact__cap">N</span>orthern<span class="contact__cap">N</span>ests.example</div>
      <div>www.<span class="contact__cap">G</span>et<span class="contact__cap">N</span>orthern<span class="contact__cap">N</span>ests.example</div>
    </address>
  </section>

  <section class="card card--back">
    <div class="safe-guide"></div>
    <span class="crop-mark crop-mark--tl"></span>
    <span class="crop-mark crop-mark--tr"></span>
    <span class="crop-mark crop-mark--bl"></span>
    <span class="crop-mark crop-mark--br"></span>

    <div class="brand-frame">
      <p class="brand brand--back">Northnest<br>Realty</p>
    </div>
  </section>
</body>
</html>
```